Project Title:
Dental Implant Overdenture Flyer (Retirement Village Target)
Objective:
Create a clean, trustworthy, and reassuring flyer aimed at older adults (60–85 years old) who struggle with loose dentures. The goal is to educate them about implant-retained “clip-on” dentures and encourage them to book a consultation.
Tone & Feel:
Warm, caring, non-intimidating
Premium but not “salesy”
Medical but easy to understand
Focus on improving quality of life (confidence, eating, comfort)
Target Audience:
Retirees / pensioners
Existing denture wearers
People frustrated with loose or uncomfortable dentures
Key Message:
“You don’t have to live with loose dentures anymore.”
Design Style:
Clean, minimal, modern
Soft colours (blues, greens, warm neutrals)
Easy-to-read large font
High contrast for older eyes
Avoid clutter
Imagery Suggestions:
Smiling older adults (natural, not stocky/overly staged)
Before/after lifestyle (eating, laughing, socialising)
Simple diagram showing denture clipping onto implants
Avoid graphic surgical images
Layout Suggestions:
A5 or DL flyer
Clear sections with headings
Icons for benefits
Strong call-to-action at bottom
HEADLINE (big and bold)
Tired of Loose Dentures?
Discover Secure “Clip-On” Teeth
🔹 PROBLEM SECTION
Do your dentures:
Slip or move when eating?
Make it hard to chew certain foods?
Feel uncomfortable or loose?
Affect your confidence when speaking or smiling?
You’re not alone — and there is a better solution.
🔹 SOLUTION SECTION
Implant-Retained “Clip-On” Dentures
We can secure your denture using just 2 dental implants, allowing your teeth to:
✔ Stay firmly in place
✔ Improve your ability to eat
✔ Feel more comfortable
✔ Boost your confidence
🔹 SIMPLE EXPLANATION (very important)
Small titanium implants are gently placed in the jaw.
Your denture then clips securely onto them, stopping movement.
🔹 PRICE SECTION (highlight this clearly)
$12,000
Includes:
2 dental implants
A brand new custom overdenture
Does not include sedation or extractions (if needed)
🔹 SEDATION
Sedation is available for comfort.
If you hold a pensioner card, you may receive a significant Vantacor rebate, often resulting in minimal out-of-pocket costs for sedation.
🔹 TRUST / REASSURANCE
Experienced implant clinician
Gentle, patient-focused care
Modern technology and techniques
🔹 CALL TO ACTION (VERY IMPORTANT)
Book a Free Consultation
📞 Call: 08 9351 4276
🌐 Visit: www.bravonclinic.com.au
📍 Located near Tallowmere shopping centre
🔹 OPTIONAL TAGLINE
Eat Better. Feel Better. Smile with Confidence Again.
Please include some photos to illustrate what a clip on denture looks like with two implants.

```html
<!DOCTYPE html>
<html lang="en">
<head>
<meta charset="utf-8">
<title>Clip-On Dentures Flyer – Bravon Clinic</title>
<link rel="stylesheet" href="https://fonts.googleapis.com/css2?family=Arimo:ital,wght@0,400;0,700;1,400;1,700&family=Chewy&display=swap">
<style>
  :root {
    --cream-yellow: #fcf5ae;
    --brown: #8a5b2e;
    --ink: #1d1d1d;
    --green: #3fb170;
    --green-soft: #4fbc80;
    --green-title: #17964a;
    --orange: #f9b458;
    --orange-text: #f3951c;
    --orange-pill: #f7a43a;
    --blue: #2aa6c6;
    --blue-light: #52c0dd;
    --white: #ffffff;
    --ghost: rgba(255,255,255,0.45);
  }
  * { box-sizing: border-box; margin: 0; padding: 0; }
  html, body { width: 1200px; height: 2398px; overflow: hidden; background: var(--white); }
  .flyer {
    position: relative; width: 1200px; height: 2398px; overflow: hidden;
    font-family: "Arimo", Arial, sans-serif; color: var(--ink); background: var(--white);
  }
  .abs { position: absolute; }
  .nowrap { white-space: nowrap; }

  /* Header */
  .hero-band { left: 0; top: 0; width: 1200px; height: 207px; background: var(--cream-yellow); }
  .hero-title {
    left: 0; top: 18px; width: 960px; text-align: center; white-space: nowrap;
    font-family: "Chewy", cursive; font-weight: 400; font-size: 70px; line-height: 84px; color: var(--brown);
  }
  .clinician-photo {
    left: 985px; top: 4px; width: 196px; height: 196px; border-radius: 50%;
    background: radial-gradient(circle at 50% 40%, #e9c4a6, #b98a6a 70%, #f3f3f3 71%);
  }

  /* Headline */
  .headline-left {
    left: 40px; top: 228px; width: 430px; text-align: center;
    font-weight: 700; font-size: 56px; line-height: 66px;
  }
  .headline-arrow { left: 492px; top: 240px; }
  .headline-right {
    left: 600px; top: 228px; width: 580px; text-align: center;
    font-weight: 700; font-style: italic; font-size: 62px; line-height: 68px; color: var(--green-title);
  }

  /* Problem */
  .problem-shape { left: 0; top: 397px; }
  .problem-label {
    left: 0; top: 413px; width: 1200px; text-align: center;
    color: var(--white); font-weight: 700; font-size: 31px; letter-spacing: 1px;
  }
  .problem-box {
    left: 249px; top: 467px; width: 748px; height: 180px; background: var(--white);
    text-align: center; font-size: 29px; line-height: 39px; padding-top: 12px;
  }
  .question { top: 470px; font-weight: 700; font-size: 150px; line-height: 150px; }
  .question--left { left: 40px; }
  .question--right { left: 1070px; }
  .not-alone {
    left: 0; top: 688px; width: 1200px; text-align: center;
    color: var(--orange-text); font-weight: 700; font-size: 35px;
  }

  /* Solution */
  .solution-panel { left: 0; top: 757px; width: 757px; height: 360px; background: var(--green-soft); }
  .side-label {
    position: absolute; transform-origin: 0 0; transform: rotate(-90deg);
    font-weight: 700; font-size: 34px; letter-spacing: 2px; color: var(--ghost); white-space: nowrap;
  }
  .solution-panel .side-label { left: 6px; top: 290px; }
  .solution-title {
    left: 55px; top: 18px; color: var(--white); font-weight: 700; font-size: 35px; white-space: nowrap;
  }
  .solution-intro {
    left: 55px; top: 62px; color: var(--white); font-style: italic; font-size: 31px; line-height: 38px; white-space: nowrap;
  }
  .benefit-list { left: 58px; top: 150px; list-style: none; font-size: 33px; line-height: 48px; }
  .benefit-list li::before {
    content: ""; display: inline-block; width: 16px; height: 16px; border-radius: 50%;
    background: var(--ink); margin-right: 12px; vertical-align: 4px;
  }
  .diagram {
    left: 750px; top: 760px; width: 450px; height: 590px; border-radius: 40px;
    background: radial-gradient(ellipse at 55% 45%, #f3d6d0 0%, #e7a9a3 45%, #ffffff 75%);
  }

  /* How it works */
  .how-panel { left: 0; top: 1145px; width: 757px; height: 199px; background: var(--orange); }
  .how-panel .side-label { left: 6px; top: 195px; font-size: 30px; line-height: 32px; }
  .how-text { left: 110px; top: 16px; font-size: 33px; line-height: 45px; white-space: nowrap; }

  /* Price */
  .price-band { left: 0; top: 1375px; width: 1200px; height: 198px; background: var(--green); }
  .price-band .side-label { left: 14px; top: 175px; font-size: 44px; letter-spacing: 2px; }
  .price-amount {
    left: 62px; top: 34px; color: var(--white); font-weight: 700; font-size: 112px; line-height: 120px; white-space: nowrap;
  }
  .price-amount .currency { font-size: 46px; vertical-align: -4px; margin-right: 4px; }
  .price-box { background: var(--white); font-size: 29px; line-height: 33px; padding: 8px 12px; white-space: nowrap; }
  .price-box--includes { left: 461px; top: 22px; width: 330px; height: 157px; text-align: right; }
  .price-box--excludes { left: 812px; top: 34px; width: 370px; height: 145px; padding-top: 34px; }
  .pill {
    background: var(--orange-pill); color: var(--white); font-size: 28px; line-height: 40px;
    padding: 0 18px; border-radius: 20px; white-space: nowrap;
  }
  .pill--includes { left: 418px; top: 110px; transform: rotate(-8deg); }
  .pill--excludes { left: 812px; top: -6px; transform: rotate(-6deg); }

  /* Sedation */
  .sedation-title {
    left: 50px; top: 1596px; color: var(--orange-text); font-weight: 700; font-style: italic; font-size: 38px; white-space: nowrap;
  }
  .sedation-text { left: 20px; top: 1644px; width: 740px; text-align: right; font-size: 31px; line-height: 43px; white-space: nowrap; }

  /* Why choose */
  .why-panel { left: 0; top: 1781px; width: 1108px; height: 198px; background: var(--orange); }
  .why-panel .side-label { left: 8px; top: 186px; font-size: 26px; line-height: 28px; letter-spacing: 1px; }
  .why-list { left: 118px; top: 14px; list-style: none; font-size: 35px; line-height: 44px; white-space: nowrap; }
  .why-list li::before { content: "❖"; margin-right: 4px; }
  .people-photo {
    left: 775px; top: 1578px; width: 425px; height: 342px; border-radius: 48%;
    background: radial-gradient(ellipse at 50% 45%, #f0cdb5, #d7a585 55%, rgba(255,255,255,0) 72%);
  }

  /* Call to action */
  .cta-line {
    height: 48px; line-height: 48px; transform: rotate(-13deg); transform-origin: 0 50%;
    color: var(--blue-light); font-weight: 700; font-size: 48px; white-space: nowrap;
  }
  .cta-line--book { left: 15px; top: 2062px; }
  .cta-line--free { left: 44px; top: 2128px; }
  .cta-line--consult { left: 16px; top: 2201px; }
  .cta-lines { left: 0; top: 2100px; }
  .phone-icon { left: 220px; top: 2008px; }
  .phone-box {
    left: 286px; top: 2016px; width: 536px; height: 82px; background: var(--blue);
    color: var(--white); font-weight: 700; font-size: 70px; line-height: 82px; text-align: center; white-space: nowrap;
  }
  .brand { left: 858px; top: 2030px; display: flex; align-items: center; gap: 14px; white-space: nowrap; }
  .brand-dot { width: 50px; height: 50px; border-radius: 50%; background: var(--blue); flex: none; }
  .brand-name { font-weight: 700; font-size: 40px; line-height: 50px; color: var(--blue); }
  .web-icon { left: 552px; top: 2134px; }
  .web-text { left: 642px; top: 2143px; font-size: 40px; line-height: 48px; white-space: nowrap; }
  .pin-icon { left: 461px; top: 2196px; }
  .location-text { left: 535px; top: 2220px; font-style: italic; font-size: 31px; line-height: 38px; white-space: nowrap; }

  /* Footer */
  .footer-band { left: 0; top: 2274px; width: 1200px; height: 124px; background: var(--cream-yellow); }
  .footer-tagline {
    left: 0; top: 2304px; width: 1200px; text-align: center; white-space: nowrap;
    font-family: "Chewy", cursive; font-weight: 400; font-size: 48px; line-height: 64px; color: var(--brown);
  }
</style>
</head>
<body>
<main class="flyer">

  <header>
    <div class="abs hero-band"></div>
    <h1 class="abs hero-title">You don’t have to live with<br>loose dentures anymore.</h1>
    <div class="abs clinician-photo" role="img" aria-label="Portrait photo of the smiling implant clinician"></div>
  </header>

  <section class="headline">
    <p class="abs headline-left">Tired of Loose<br>Dentures?</p>
    <svg class="abs headline-arrow" width="96" height="128" viewBox="0 0 96 128" aria-hidden="true">
      <polygon points="0,0 96,64 0,128" fill="#1a9a45"/>
    </svg>
    <h2 class="abs headline-right">Discover Secure<br>“Clip-On” Teeth</h2>
  </section>

  <section class="problem">
    <svg class="abs problem-shape" width="1200" height="258" viewBox="0 0 1200 258" aria-hidden="true">
      <path d="M175 0 H1025 Q975 129 1025 258 H175 Q225 129 175 0 Z" fill="#f9b458"/>
    </svg>
    <p class="abs problem-label">DO YOUR DENTURES</p>
    <div class="abs problem-box">
      <p>Slip or move when eating</p>
      <p>Make it hard to chew certain foods</p>
      <p>Feel loose or uncomfortable</p>
      <p>Affect your confidence when speaking or smiling</p>
    </div>
    <span class="abs question question--left">?</span>
    <span class="abs question question--right">?</span>
    <p class="abs not-alone">YOU’RE NOT ALONE — AND THERE IS A BETTER SOLUTION</p>
  </section>

  <section class="abs solution-panel">
    <span class="side-label">SOLUTION</span>
    <h3 class="abs solution-title">Implant-Retained “Clip-On” Dentures</h3>
    <p class="abs solution-intro">With just 2 small dental implants,<br>we can secure your denture so it can:</p>
    <ul class="abs benefit-list">
      <li>Stay firmly in place</li>
      <li>Improve your ability to eat</li>
      <li>Feel more comfortable</li>
      <li>Boost your confidence</li>
    </ul>
  </section>

  <div class="abs diagram" role="img" aria-label="Illustration of an upper denture clipping onto two dental implants in the jaw"></div>

  <section class="abs how-panel">
    <span class="side-label">HOW IT<br>WORKS</span>
    <p class="abs how-text">Small titanium implants<br>are gently placed in the<br>jaw. Your denture then clips securely<br>onto them – stopping movement.</p>
  </section>

  <section class="abs price-band">
    <span class="side-label">PRICE</span>
    <p class="abs price-amount"><span class="currency">$</span>12,000</p>
    <div class="abs price-box price-box--includes">
      <p>☞ 2 dental implants</p>
      <p>☞ A brand-new</p>
      <p>custom</p>
      <p>overdenture</p>
    </div>
    <span class="abs pill pill--includes">INCLUDES</span>
    <div class="abs price-box price-box--excludes">
      <p>☞ Sedation (optional)</p>
      <p>☞ Extractions</p>
      <p>&nbsp;&nbsp;&nbsp;&nbsp;(if needed)</p>
    </div>
    <span class="abs pill pill--excludes">NOT INCLUDES</span>
  </section>

  <section class="sedation">
    <h3 class="abs sedation-title">SEDATION is available for comfort.</h3>
    <p class="abs sedation-text">If you hold a pensioner card, you may receive<br>a significant Vantacor rebate, often resulting<br>in minimal out-of-pocket costs for sedation.</p>
  </section>

  <section class="abs why-panel">
    <span class="side-label">WHY<br>CHOOSE<br>US</span>
    <ul class="abs why-list">
      <li>Experienced implant clinician</li>
      <li>Gentle, patient-focused care</li>
      <li>Modern technology and techniques</li>
      <li>Supportive team who take their time with you</li>
    </ul>
  </section>

  <div class="abs people-photo" role="img" aria-label="Photo of two smiling older women"></div>

  <section class="cta">
    <p class="abs cta-line cta-line--book">BOOK</p>
    <p class="abs cta-line cta-line--free">A FREE</p>
    <p class="abs cta-line cta-line--consult">CONSULTATION</p>
    <svg class="abs cta-lines" width="460" height="174" viewBox="0 0 460 174" aria-hidden="true">
      <g stroke="#52c0dd" stroke-width="4">
        <line x1="180" y1="115" x2="420" y2="60"/>
        <line x1="20" y1="168" x2="430" y2="74"/>
      </g>
    </svg>
    <svg class="abs phone-icon" width="96" height="96" viewBox="0 0 96 96" aria-hidden="true">
      <circle cx="48" cy="48" r="42" fill="#fff" stroke="#1d1d1d" stroke-width="5"/>
      <path d="M36 24 C28 30 26 40 30 52 C34 64 42 72 54 74 L58 66 L50 60 L45 64 C40 60 38 54 37 47 L43 44 L42 34 Z" fill="#1d1d1d"/>
    </svg>
    <p class="abs phone-box">08 9351 4276</p>
    <div class="abs brand">
      <span class="brand-dot"></span>
      <span class="brand-name">Bravon Clinic</span>
    </div>
    <svg class="abs web-icon" width="64" height="64" viewBox="0 0 40 40" aria-hidden="true">
      <g fill="none" stroke="#2aa6c6" stroke-width="2.5">
        <circle cx="20" cy="20" r="17"/>
        <ellipse cx="20" cy="20" rx="7" ry="17"/>
        <line x1="3" y1="20" x2="37" y2="20"/>
        <line x1="6" y1="11" x2="34" y2="11"/>
        <line x1="6" y1="29" x2="34" y2="29"/>
      </g>
    </svg>
    <p class="abs web-text">www.bravonclinic.com.au</p>
    <svg class="abs pin-icon" width="46" height="58" viewBox="0 0 40 52" aria-hidden="true">
      <path d="M20 3 C10 3 4 10 4 19 C4 31 20 48 20 48 C20 48 36 31 36 19 C36 10 30 3 20 3 Z" fill="none" stroke="#2aa6c6" stroke-width="3.5"/>
      <circle cx="20" cy="19" r="6" fill="none" stroke="#2aa6c6" stroke-width="3.5"/>
    </svg>
    <p class="abs location-text">Located near Tallowmere shopping centre</p>
  </section>

  <footer>
    <div class="abs footer-band"></div>
    <p class="abs footer-tagline">Eat Better. Feel Better. Smile with Confidence Again.</p>
  </footer>

</main>
</body>
</html>
```